VELNA BROCADE

Project name: “Velna Brocade” website
Objective: To create an elegant website,
intuitive and responsive to present this
what is “Velna Brocade”
See attached specifications.

```html
<!DOCTYPE html>
<html lang="en">
<head>
<meta charset="utf-8">
<title>Velna Brocade</title>
<link href="https://fonts.googleapis.com/css2?family=Poppins:wght@400;500;600;700;800&display=swap" rel="stylesheet">
<style>
:root{
  --green:#3e5a3d;
  --green-dark:#324a32;
  --sage:#dce4dc;
  --sage-line:#cfdccd;
  --grey-bg:#efeff1;
  --text:#2b2b2b;
  --white:#ffffff;
  --gold:#e2a623;
}
*{box-sizing:border-box;margin:0;padding:0}
html,body{width:1200px;height:3283px;overflow:hidden;background:var(--white);font-family:"Poppins",sans-serif;color:var(--text)}
.page{position:relative;width:1200px;height:3283px;overflow:hidden}
.abs{position:absolute}
.center{left:0;width:1200px;text-align:center}

/* header */
.header{left:0;top:0;width:1200px;height:129px;background:var(--green);z-index:5}
.logo-dip{left:510px;top:60px;width:180px;height:116px;border-radius:0 0 90px 90px;background:var(--green);z-index:5}
.social{width:42px;height:42px;border-radius:50%;background:rgba(255,255,255,.14);z-index:6}
.social.active{background:var(--sage)}
.nav{top:90px;font-size:14px;font-weight:600;color:var(--white);z-index:6;text-transform:uppercase;letter-spacing:.2px;white-space:nowrap}
.nav.current{border-bottom:2px solid var(--white);padding-bottom:1px}
.nav-divider{left:980px;top:80px;width:1px;height:38px;background:rgba(255,255,255,.3);z-index:6}
.phone-pill{left:882px;top:19px;width:173px;height:47px;border-radius:24px;background:var(--sage);z-index:6;font-size:15px;font-weight:600;color:var(--green);display:flex;align-items:center;justify-content:center;gap:8px;white-space:nowrap}
.brand-mark{left:567px;top:22px;width:66px;height:66px;border-radius:50%;border:2px solid var(--white);z-index:6}
.brand-name{top:116px;font-size:18px;font-weight:500;letter-spacing:3px;color:var(--white);z-index:6;white-space:nowrap}

/* hero */
.hero{left:0;top:129px;width:1200px;height:640px}
.hero-title{top:282px;left:250px;width:700px;text-align:center;color:var(--white);font-size:36px;font-weight:700;line-height:48px;text-transform:uppercase;text-shadow:0 2px 8px rgba(0,0,0,.35)}
.hero-text{top:432px;left:240px;width:720px;text-align:center;color:var(--white);font-size:21px;line-height:30px;text-shadow:0 2px 6px rgba(0,0,0,.4)}
.btn{height:44px;width:150px;border-radius:22px;background:var(--green);color:var(--white);font-size:15px;font-weight:600;display:flex;align-items:center;justify-content:center;text-transform:uppercase}
.arrow{width:30px;height:30px;border-radius:50%;display:flex;align-items:center;justify-content:center}
.arrow.light{background:var(--white)}
.arrow.dim{background:rgba(255,255,255,.45)}
.arrow.grey{background:#8a8a8a}
.arrow.dark{background:var(--green)}

/* welcome */
.welcome-bg{left:0;top:600px;width:1200px;height:1640px;background:linear-gradient(180deg,#e6e7e8 0%,#efeff1 40%,var(--grey-bg) 100%)}
.emblem-ring{left:542px;top:697px;width:116px;height:116px;border-radius:50%;background:var(--grey-bg);border:2px solid #d5d8d5}
.emblem{left:566px;top:721px;width:68px;height:68px;border-radius:50%;background:var(--green);border:3px solid var(--sage-line)}
.kicker{top:844px;font-size:24px;font-weight:500;color:var(--green);text-transform:uppercase}
.section-title{font-size:50px;font-weight:800;color:var(--text);text-transform:uppercase;letter-spacing:.5px;white-space:nowrap}
.welcome-text{left:170px;width:860px;top:950px;text-align:center;font-size:18.5px;line-height:26px;color:#333}
.feature{width:296px;height:296px;border-radius:50%;border:4px solid var(--white);box-shadow:0 6px 14px rgba(0,0,0,.12);overflow:hidden}
.feature-label{left:0;bottom:0;width:100%;height:72px;background:rgba(62,90,61,.9);color:var(--white);font-size:15px;font-weight:600;text-align:center;padding-top:22px;text-transform:uppercase}
.feature-overlay{left:22px;top:22px;width:244px;height:244px;border-radius:50%;background:rgba(62,90,61,.9);color:var(--white);text-align:center;padding:52px 26px 0}
.feature-overlay h3{font-size:15px;font-weight:600;margin-bottom:10px}
.feature-overlay p{font-size:13px;line-height:20px;opacity:.92}
.feature-overlay span{display:inline-block;margin-top:12px;font-size:12px;font-weight:600;text-decoration:underline}

/* feed */
.subtitle{font-size:19px;color:#333}
.post{width:448px;height:394px;border-radius:26px;background:var(--white);border:2px solid #e2e4e2;overflow:hidden}
.avatar{left:16px;top:18px;width:54px;height:54px;border-radius:50%;background:linear-gradient(160deg,#c9b59a,#8f7a5c)}
.post-name{left:82px;top:22px;font-size:16px;font-weight:600}
.post-org{left:82px;top:46px;font-size:13px;color:#444}
.like{left:324px;top:28px;width:108px;height:30px;border:1px solid #ccc;border-radius:4px;font-size:12.5px;font-weight:600;display:flex;align-items:center;justify-content:center;gap:5px}
.post-text{left:16px;top:82px;width:418px;font-size:13.2px;line-height:21px;color:#333}
.post-photo{left:0;top:154px;width:448px;height:240px;border-radius:22px 22px 0 0}

/* testimonial */
.testimonial{left:180px;top:2431px;width:840px;height:383px;border-radius:48px;overflow:hidden;background:var(--sage)}
.quote-mark{left:42px;top:32px;font-size:96px;line-height:96px;font-weight:700;color:var(--green);font-family:"Georgia",serif}
.client{left:42px;top:100px;font-size:15px}
.client b{font-weight:700}
.stars{left:42px;top:126px;color:var(--gold);font-size:13px;letter-spacing:1px}
.testimonial p{font-size:16px;line-height:24px;color:#333}
.dot{width:12px;height:12px;border-radius:50%;border:1.5px solid #666}
.dot.on{background:var(--green);border-color:var(--green)}

/* footer */
.footer-bar{left:0;top:3230px;width:1200px;height:53px;background:var(--green-dark)}
.foot-head{font-size:15px;font-weight:600;color:var(--white);text-transform:uppercase;border-bottom:2px solid var(--white);padding-bottom:2px;white-space:nowrap}
.foot-link{font-size:13.5px;color:var(--white);white-space:nowrap}
.contact-ico{width:26px;height:26px;border-radius:50%;background:rgba(255,255,255,.15);display:flex;align-items:center;justify-content:center}
.subscribe{left:836px;top:3065px;width:220px;height:34px;border-radius:17px;background:var(--white);overflow:hidden}
.subscribe span{position:absolute;left:16px;top:9px;font-size:11px;color:#555}
.subscribe .send{left:176px;top:0;width:44px;height:34px;background:var(--sage)}
.foot-social{width:42px;height:42px;border-radius:50%;background:rgba(255,255,255,.14)}
.foot-social.active{background:var(--sage)}
.foot-brand{left:104px;top:3158px;width:260px;text-align:center;font-size:19px;font-weight:500;letter-spacing:3px;color:var(--white);white-space:nowrap}
.copyright{left:518px;top:3246px;font-size:12.5px;color:var(--white);white-space:nowrap}
</style>
</head>
<body>
<div class="page">

  <div class="abs welcome-bg"></div>

  <!-- hero -->
  <svg class="abs hero" viewBox="0 129 1200 640" width="1200" height="640" role="img" aria-label="Aerial photo of a riverside village with red-tiled roofs and green trees">
    <defs>
      <linearGradient id="heroGrad" x1="0" y1="0" x2="0" y2="1">
        <stop offset="0" stop-color="#7c7453"/>
        <stop offset=".45" stop-color="#5a5238"/>
        <stop offset="1" stop-color="#6b5a44"/>
      </linearGradient>
    </defs>
    <path d="M0 129 H1200 V612 Q600 900 0 612 Z" fill="url(#heroGrad)"/>
    <path d="M0 612 Q600 900 1200 612" fill="none" stroke="#d6e0d4" stroke-width="10"/>
  </svg>

  <div class="abs hero-title">Experience the Limousin differently — authentic nature, calm living, and local heritage</div>
  <div class="abs hero-text">Velna Brocade promotes the beauty of the Limousin region and supports families, couples, and future residents looking for the right land or project.</div>
  <div class="abs btn" style="left:525px;top:544px">Learn More</div>
  <div class="abs arrow dim" style="left:56px;top:371px"><svg width="14" height="14" viewBox="0 0 14 14"><path d="M9 2 4 7l5 5" fill="none" stroke="#333" stroke-width="2.5"/></svg></div>
  <div class="abs arrow light" style="left:1113px;top:371px"><svg width="14" height="14" viewBox="0 0 14 14"><path d="M5 2l5 5-5 5" fill="none" stroke="#333" stroke-width="2.5"/></svg></div>

  <!-- header -->
  <div class="abs header"></div>
  <div class="abs logo-dip"></div>
  <div class="abs social" style="left:143px;top:22px"></div>
  <div class="abs social active" style="left:192px;top:22px"></div>
  <div class="abs social" style="left:240px;top:22px"></div>
  <div class="abs nav current" style="left:143px">Home</div>
  <div class="abs nav" style="left:210px">Who we are</div>
  <div class="abs nav" style="left:328px">Land prospecting</div>
  <div class="abs nav" style="left:748px">Our features</div>
  <div class="abs nav" style="left:878px">Contact</div>
  <div class="abs nav-divider"></div>
  <div class="abs nav" style="left:1011px">Eng ⌄</div>
  <div class="abs phone-pill">
    <svg width="14" height="14" viewBox="0 0 24 24"><path d="M6.6 10.8a15 15 0 0 0 6.6 6.6l2.2-2.2a1 1 0 0 1 1-.25 11 11 0 0 0 3.6.6 1 1 0 0 1 1 1V20a1 1 0 0 1-1 1A17 17 0 0 1 3 4a1 1 0 0 1 1-1h3.5a1 1 0 0 1 1 1c0 1.25.2 2.45.6 3.6a1 1 0 0 1-.25 1z" fill="#3e5a3d"/></svg>
    +1 555 010 2040
  </div>
  <div class="abs brand-mark"></div>
  <div class="abs center brand-name">VELNA BROCADE</div>

  <!-- welcome -->
  <div class="abs emblem-ring"></div>
  <div class="abs emblem"></div>
  <div class="abs center kicker">Welcome to</div>
  <div class="abs center section-title" style="top:872px">VELNA BROCADE</div>
  <p class="abs welcome-text">Lorem ipsum dolor sit amet, consectetur adip elit, sed do eiusmod tempor incididunt ut labore et dolore magna aliqua. Ut enim ad minim veniam, quis nostrud exercitation ulla laboris nisi ut aliquip ex ea commodo conse dolore euquat. Duis aute irure dolor in reprehenderit in volu ptate velit esse cillum dolore eu fugiat nulla quis nostrud pariatur. Excepteur sint occaecat cupidatat non proident, sunt in culpa qui officia deserunt.</p>
  <div class="abs btn" style="left:525px;top:1114px">Learn More</div>

  <svg class="abs" style="left:0;top:1260px" width="1200" height="200" viewBox="0 1260 1200 200">
    <path d="M0 1440 Q600 1180 1200 1440" fill="none" stroke="var(--green)" stroke-width="12"/>
  </svg>

  <div class="abs feature" style="left:142px;top:1111px" role="img" aria-label="Two hikers with backpacks on a sunlit coastal cliff path">
    <div class="abs" style="inset:0;background:linear-gradient(170deg,#e4d7a8 0%,#a79a5c 45%,#5d6a35 100%)"></div>
    <div class="abs feature-label">Nature &amp; Hiking</div>
  </div>
  <div class="abs feature" style="left:452px;top:1208px" role="img" aria-label="Stone heritage village street">
    <div class="abs" style="inset:0;background:linear-gradient(170deg,#7d8a74 0%,#5f6a58 50%,#8c8676 100%)"></div>
    <div class="abs feature-overlay">
      <h3>HERITAGE</h3>
      <p>Lorem ipsum dolor sit amet, consectetur adip elit, sed doe eiusmod tempor incididunt labore sit dolorea.</p>
      <span>LEARN MORE</span>
    </div>
  </div>
  <div class="abs feature" style="left:762px;top:1111px" role="img" aria-label="Family on a pier looking over a lake and hills">
    <div class="abs" style="inset:0;background:linear-gradient(180deg,#e9cfa6 0%,#9db0c0 40%,#5b7a6a 70%,#3f6a8c 100%)"></div>
    <div class="abs feature-label">Family Life</div>
  </div>

  <!-- feed -->
  <div class="abs center section-title" style="top:1552px">Stay Connected</div>
  <div class="abs center subtitle" style="top:1626px">Integrated social feed showing recent posts, announcements, and updates.</div>

  <div class="abs post" style="left:143px;top:1683px">
    <div class="abs avatar" role="img" aria-label="Profile photo"></div>
    <div class="abs post-name">Maren Aldous</div>
    <div class="abs post-org">Velna Brocade</div>
    <div class="abs like">👍 Like Page</div>
    <p class="abs post-text">Lorem ipsum dolor sit amet, consectetur adip elit, sed do eiusmo tempor incididunt ut labore et dolore magna aliqua. Ut enim ad minim veniam, quis nostrud.</p>
    <div class="abs post-photo" role="img" aria-label="Couple of hikers resting on a mountain ridge" style="background:linear-gradient(160deg,#a8b6b8 0%,#6f7f78 45%,#4c5a4e 100%)"></div>
  </div>
  <div class="abs post" style="left:610px;top:1683px">
    <div class="abs avatar" role="img" aria-label="Profile photo"></div>
    <div class="abs post-name">Maren Aldous</div>
    <div class="abs post-org">Velna Brocade</div>
    <div class="abs like">👍 Like Page</div>
    <p class="abs post-text">Lorem ipsum dolor sit amet, consectetur adip elit, sed do eiusmo tempor incididunt ut labore et dolore magna aliqua. Ut enim ad minim veniam, quis nostrud.</p>
    <div class="abs post-photo" role="img" aria-label="Riverside stone village with church tower and trees" style="background:linear-gradient(180deg,#b7ccd8 0%,#6f8a5a 40%,#7d7664 60%,#4d5f4a 100%)"></div>
  </div>
  <div class="abs arrow grey" style="left:56px;top:1865px"><svg width="14" height="14" viewBox="0 0 14 14"><path d="M9 2 4 7l5 5" fill="none" stroke="#fff" stroke-width="2.5"/></svg></div>
  <div class="abs arrow dark" style="left:1113px;top:1865px"><svg width="14" height="14" viewBox="0 0 14 14"><path d="M5 2l5 5-5 5" fill="none" stroke="#fff" stroke-width="2.5"/></svg></div>

  <svg class="abs" style="left:0;top:2070px" width="1200" height="260" viewBox="0 2070 1200 260">
    <path d="M0 2090 Q600 2380 1200 2090 V2330 H0 Z" fill="var(--white)"/>
    <path d="M0 2090 Q600 2380 1200 2090" fill="none" stroke="var(--green)" stroke-width="10"/>
  </svg>
  <div class="abs" style="left:0;top:2240px;width:1200px;height:700px;background:var(--white)"></div>

  <!-- testimonials -->
  <div class="abs center section-title" style="top:2332px">What our clients say</div>
  <div class="abs testimonial">
    <div class="abs quote-mark">“</div>
    <div class="abs client"><b>– ODILE,</b> Lakeview, OR</div>
    <div class="abs stars">★★★★★</div>
    <p class="abs" style="left:42px;top:156px;width:360px">Sed ut perspiciatis unde omnis iste natus error sit voluptatem accusantium doloremque laudantium, totam rem aperiam, eaque ipsa quae ab illo inventore dicta sunt explicabo.</p>
    <p class="abs" style="left:42px;top:290px;width:360px">Sed ut perspiciatis unde omnis iste natus error sit voluptatem accusantium doloremque laudantiumea.</p>
    <div class="abs" style="left:420px;top:0;width:420px;height:383px;background:linear-gradient(160deg,#d8c8b4 0%,#ece7e0 50%,#f4f2ef 100%)" role="img" aria-label="Portrait of a smiling client"></div>
  </div>
  <div class="abs dot" style="left:565px;top:2849px"></div>
  <div class="abs dot on" style="left:584px;top:2849px"></div>
  <div class="abs dot" style="left:603px;top:2849px"></div>
  <div class="abs dot" style="left:623px;top:2849px"></div>

  <!-- footer -->
  <svg class="abs" style="left:0;top:2920px" width="1200" height="320" viewBox="0 2920 1200 320">
    <path d="M0 3083 Q600 2820 1200 3083 V3240 H0 Z" fill="var(--green)"/>
    <path d="M0 3083 Q600 2820 1200 3083" fill="none" stroke="#d6e0d4" stroke-width="10"/>
  </svg>
  <div class="abs" style="left:190px;top:3055px;width:88px;height:88px;border-radius:50%;border:2px solid var(--white)"></div>
  <div class="abs foot-brand">VELNA BROCADE</div>

  <div class="abs foot-head" style="left:383px;top:3020px">Site Map</div>
  <div class="abs foot-link" style="left:383px;top:3062px">Home</div>
  <div class="abs foot-link" style="left:383px;top:3090px">Approach</div>
  <div class="abs foot-link" style="left:383px;top:3119px">Programs</div>
  <div class="abs foot-link" style="left:383px;top:3148px">About</div>
  <div class="abs foot-link" style="left:383px;top:3176px">Contact</div>

  <div class="abs foot-head" style="left:526px;top:3020px">Contact Info</div>
  <div class="abs contact-ico" style="left:522px;top:3064px"><svg width="11" height="11" viewBox="0 0 24 24"><path d="M6.6 10.8a15 15 0 0 0 6.6 6.6l2.2-2.2a1 1 0 0 1 1-.25 11 11 0 0 0 3.6.6 1 1 0 0 1 1 1V20a1 1 0 0 1-1 1A17 17 0 0 1 3 4a1 1 0 0 1 1-1h3.5a1 1 0 0 1 1 1c0 1.25.2 2.45.6 3.6a1 1 0 0 1-.25 1z" fill="#fff"/></svg></div>
  <div class="abs foot-link" style="left:562px;top:3067px">+1 555 010 2040</div>
  <div class="abs contact-ico" style="left:522px;top:3107px"><svg width="11" height="11" viewBox="0 0 24 24"><path d="M2 5h20v14H2z" fill="#fff"/><path d="M2 5l10 8 10-8" fill="none" stroke="#3e5a3d" stroke-width="2"/></svg></div>
  <div class="abs foot-link" style="left:562px;top:3110px">contact@velnabrocade.com</div>
  <div class="abs contact-ico" style="left:522px;top:3148px"><svg width="11" height="11" viewBox="0 0 24 24"><path d="M12 2a7 7 0 0 0-7 7c0 5 7 13 7 13s7-8 7-13a7 7 0 0 0-7-7zm0 9.5a2.5 2.5 0 1 1 0-5 2.5 2.5 0 0 1 0 5z" fill="#fff"/></svg></div>
  <div class="abs foot-link" style="left:562px;top:3151px">123 Sed ut perspiciatis unde, Valmont</div>

  <div class="abs foot-head" style="left:836px;top:3020px">Subscribe</div>
  <div class="abs subscribe">
    <span>✉ Email Address</span>
    <div class="abs send"><svg style="position:absolute;left:14px;top:10px" width="15" height="15" viewBox="0 0 24 24"><path d="M22 2 2 10l7 3 3 7z" fill="#3e5a3d"/></svg></div>
  </div>

  <div class="abs footer-bar"></div>
  <div class="abs copyright">© 2025 &nbsp;/&nbsp; All Rights Reserved</div>
  <div class="abs foot-social" style="left:918px;top:3235px"></div>
  <div class="abs foot-social active" style="left:965px;top:3235px"></div>
  <div class="abs foot-social" style="left:1013px;top:3235px"></div>

</div>
</body>
</html>
```